business card logos

We have two companies
1) Velmora limos and our punch line is " Don't Just Ride it. Velmora it.

2) Crestwell Hire Cars and the punch line is " Yes, your travel is our business!"
We provide chauffeured cars in Sydney for corporate travel in the city's metropolitan areas. These are very comfortable and affordable corporate cars for our most valuable clients.

Need a logo design for business cards for both which will be unique, reflects the services we offer, has to look professional.

```html
<!DOCTYPE html>
<html lang="en">
<head>
<meta charset="utf-8">
<title>Velmora limos – business cards and name</title>
<link rel="stylesheet" href="https://fonts.googleapis.com/css2?family=Cinzel:wght@400&display=swap">
<style>
  :root {
    --navy: #244a80;
    --gold: #e3a629;
    --white: #ffffff;
    --backdrop: #d9d9d9;
    --shadow: rgba(0,0,0,0.28);
  }
  * { margin: 0; padding: 0; box-sizing: border-box; }
  html, body { width: 1200px; height: 849px; overflow: hidden; }
  body {
    background: var(--backdrop);
    font-family: "Cinzel", Georgia, serif;
    font-weight: 400;
    position: relative;
  }
  .card {
    position: absolute;
    width: 460px;
    height: 262px;
    background: var(--white);
    box-shadow: 0 6px 18px var(--shadow);
    overflow: hidden;
  }
  .card svg.card-shape { position: absolute; inset: 0; }
  .card-back { left: 70px; top: 110px; }
  .card-front { left: 70px; top: 470px; }

  .company-name {
    color: var(--gold);
    font-weight: 400;
    white-space: nowrap;
    display: flex;
    align-items: center;
    gap: 10px;
    line-height: 1;
  }
  .company-name .name-dot {
    width: 0.45em; height: 0.45em;
    border-radius: 50%;
    background: var(--gold);
    flex: none;
  }
  .punchline {
    color: var(--navy);
    text-transform: uppercase;
    line-height: 1.15;
  }

  /* agent side */
  .card-back .company-name { position: absolute; left: 18px; top: 34px; font-size: 24px; }
  .card-back .punchline { position: absolute; left: 18px; top: 78px; font-size: 15px; }
  .agent {
    position: absolute; left: 222px; top: 110px; width: 218px;
    color: var(--gold); text-align: center; font-size: 19px;
    border-top: 2px solid var(--gold); border-bottom: 2px solid var(--gold);
    padding: 8px 0;
  }
  .contact {
    position: absolute; right: 14px; top: 188px;
    color: var(--white); text-align: right; font-size: 15px; line-height: 1.12;
  }

  /* company side */
  .card-front .company-name { position: absolute; left: 0; right: 0; top: 40px; justify-content: center; font-size: 36px; }
  .card-front .punchline { position: absolute; left: 0; right: 0; top: 98px; text-align: center; font-size: 16px; }
  .about {
    position: absolute; left: 20px; right: 20px; bottom: 16px;
    color: var(--white); text-align: center; font-size: 9.5px;
    line-height: 1.25; text-transform: uppercase;
  }

  /* standalone name */
  .name-lockup {
    position: absolute; left: 600px; top: 360px; width: 560px;
  }
  .name-lockup .company-name { justify-content: center; font-size: 56px; }
</style>
</head>
<body>

  <section class="card card-back" aria-label="Business card, agent side">
    <svg class="card-shape" width="460" height="262" viewBox="0 0 460 262">
      <path d="M312,0 H460 V262 H0 V212 C110,150 240,80 312,0 Z" fill="var(--gold)"/>
      <path d="M334,0 H460 V262 H0 V236 C120,170 262,90 334,0 Z" fill="var(--navy)"/>
    </svg>
    <div class="company-name"><span class="name-dot"></span>Velmora limos</div>
    <p class="punchline">Don't just ride it.<br>Velmora it.</p>
    <p class="agent">Agents Name</p>
    <p class="contact">Tel Number<br>Address<br>Email Address</p>
  </section>

  <section class="card card-front" aria-label="Business card, company side">
    <svg class="card-shape" width="460" height="262" viewBox="0 0 460 262">
      <path d="M0,188 C160,198 330,160 460,98 V262 H0 Z" fill="var(--navy)"/>
    </svg>
    <div class="company-name"><span class="name-dot"></span>Velmora limos</div>
    <p class="punchline">Don't just ride it.<br>Velmora it.</p>
    <p class="about">We provide chauffeured cars in Sydney for corporate travel in the city's metropolitan areas. These are very comfortable and affordable corporate cars for our most valuable clients.</p>
  </section>

  <section class="name-lockup" aria-label="Velmora limos">
    <div class="company-name"><span class="name-dot"></span>Velmora limos</div>
  </section>

</body>
</html>
```